DMB - Stationery Design Project

We need stationery based on our logo.

Company info :
Cabinet Durvaux & Associés
Société à responsabilité limitée au capital de 200.000 FCFP
RCS Papeete 58207K - Numéro tahiti K63095
Centre d’affaires OPALE - Rue Gaston Verdier
BP 51839 MAHANA KOLO - 98713 Papeete
Tahiti - Polynésie française
Tél : +689 40 73 16 84
Fax : +689 40 39 57 61

Industry/Entity Type

It Company

Font styles to use
Sans Serif

```html
<!DOCTYPE html>
<html lang="fr">
<head>
<meta charset="utf-8">
<title>DMB – Stationery</title>
<link rel="stylesheet" href="https://fonts.googleapis.com/css2?family=Arimo:wght@400;700&display=swap">
<style>
  :root {
    --navy: #0e2a4e;
    --slate: #8b989b;
    --ink: #2b2b2b;
    --paper: #ffffff;
    --card-fade: #eef0f1;
    --backdrop: #2b2b2b;
  }
  * { box-sizing: border-box; margin: 0; padding: 0; }
  html, body { width: 1200px; height: 1092px; overflow: hidden; }
  body { background: var(--backdrop); font-family: "Arimo", Arial, sans-serif; position: relative; color: var(--ink); }

  .wordmark { display: flex; align-items: center; gap: 14px; font-family: "Arimo", Arial, sans-serif; font-weight: 400; color: var(--navy); line-height: 1; }
  .wordmark__square { display: block; background: var(--navy); }
  .wordmark__name { letter-spacing: 2px; }

  .contact { font-family: "Arimo", Arial, sans-serif; color: var(--ink); }
  .contact dt { font-weight: 700; display: inline; }
  .contact dd { display: inline; }
  .contact dd::after { content: ""; display: block; }
  .contact__firm { font-weight: 700; color: var(--navy); }

  /* Letterhead */
  .letterhead {
    position: absolute; left: 70px; top: 52px; width: 700px; height: 990px;
    background: var(--paper); padding: 56px 56px;
  }
  .letterhead__head { display: flex; justify-content: space-between; align-items: flex-start; }
  .letterhead .wordmark { font-size: 72px; margin-top: 14px; }
  .letterhead .wordmark__square { width: 22px; height: 22px; }
  .letterhead .contact { font-size: 13px; line-height: 1.3; width: 250px; }
  .letterhead .contact__address { margin-top: 6px; font-size: 10.5px; line-height: 1.3; color: var(--slate); }
  .letter { margin-top: 70px; font-size: 12.5px; line-height: 1.22; }
  .letter p { margin-bottom: 15px; }
  .letter .qa { margin: 20px 0 22px 14px; }

  /* Business cards */
  .card { position: absolute; left: 812px; width: 340px; height: 190px; overflow: hidden; }
  .card--front { top: 300px; background: linear-gradient(180deg, var(--paper) 0%, var(--card-fade) 100%); }
  .card--front::after { content: ""; position: absolute; left: 0; right: 0; bottom: 0; height: 12px; background: var(--navy); }
  .card--front .wordmark { position: absolute; left: 28px; top: 66px; font-size: 46px; gap: 9px; }
  .card--front .wordmark__square { width: 14px; height: 14px; }
  .card__person { position: absolute; left: 200px; top: 28px; }
  .card__name { font-weight: 700; font-size: 16px; color: var(--navy); }
  .card__role { font-weight: 700; font-size: 11px; color: var(--slate); margin-top: 5px; }
  .card--front .contact { position: absolute; left: 200px; top: 100px; font-size: 9px; line-height: 1.3; }

  .card--back { top: 534px; background: var(--navy); display: flex; align-items: center; justify-content: center; }
  .card--back .wordmark { color: var(--paper); font-size: 52px; gap: 12px; }
  .card--back .wordmark__square { width: 16px; height: 16px; background: var(--paper); }
</style>
</head>
<body>

<article class="letterhead">
  <header class="letterhead__head">
    <div class="wordmark"><span class="wordmark__square"></span><span class="wordmark__name">DMB</span></div>
    <div class="contact">
      <p class="contact__firm">Cabinet Durvaux &amp; Associés</p>
      <dl>
        <dt>Phone:</dt> <dd>+689 40 73 16 84</dd>
        <dt>Fax:</dt> <dd>+689 40 39 57 61</dd>
        <dt>Email:</dt> <dd>info@dmbcabinet.pf</dd>
        <dt>Website:</dt> <dd>www.dmbcabinet.pf</dd>
      </dl>
      <address class="contact__address">Centre d’affaires OPALE - Rue Gaston Verdier<br>BP 51839 MAHANA KOLO - 98713 Papeete<br>Tahiti - Polynésie française</address>
    </div>
  </header>

  <section class="letter">
    <p>Dear<br>Sir/Madam<br>Its all sample text<br>A stationary spacetime admits a timelike Killing vector field. A static spacetime is a stationary spacetime in which the timelike Killing vector field has vanishing vorticity, or equivalently (by the Frobenius theorem) is hypersurface orthogonal.</p>
    <p>What does this mean? That a stationary spacetime is one in which you can find a family of observers who observe no changes in the gravitational field (or sources such as matter or electromagnetic fields) over time. A static spacetime is one which admits a slicing into spacelike hypersurfaces which are everywhere orthogonal to the world lines of our "bored observers".</p>
    <p>One can still imagine observers who move around an interact, or even light beams or other waves, but these are assumed to have neglible effect on the ambient gravitational field. So for example one can study scattering of waves by black holes.</p>
    <p class="qa">does static imply stationary? is the converse true?</p>
    <p class="qa">Yes. No.</p>
    <p class="qa">What are a couple of example?</p>
    <p class="qa">Some basic examples of static solutions:</p>
    <p class="qa">1. Any Weyl vacuum: see my post #12 in<br>http://www.sampleforum.org/thread.php?t=153765&amp;q=Weyl+vacuum<br>plus generalizations allowing for EM fields, scalar fields, etc.</p>
  </section>
</article>

<div class="card card--front">
  <div class="wordmark"><span class="wordmark__square"></span><span class="wordmark__name">DMB</span></div>
  <div class="card__person">
    <div class="card__name">Marc Tessier</div>
    <div class="card__role">Director</div>
  </div>
  <dl class="contact">
    <dt>Phone:</dt> <dd>+689 40 73 16 84</dd>
    <dt>Fax:</dt> <dd>+689 40 39 57 61</dd>
    <dt>Email:</dt> <dd>info@dmbcabinet.pf</dd>
    <dt>Website:</dt> <dd>www.dmbcabinet.pf</dd>
  </dl>
</div>

<div class="card card--back">
  <div class="wordmark"><span class="wordmark__square"></span><span class="wordmark__name">DMB</span></div>
</div>

</body>
</html>
```